Cat-products company needs smart, yet endearing, business card

We need a business card design for a new, but up-and-running, business based in Honolulu, Hawaii. The business is Purrlane Nest Co. Our first product is the most environmentally-friendly cat grass kit ever seen on the planet. Future products, currently in the R&D phase, will include a variety of exciting cat scratchers. We also do consulting work to help apartment-dwellers make their home more cat-friendly and, in the future, plan on doing full, custom installs of structure to create high walkways for cats.

Target Market(s)

Middle-aged, apartment-dwelling, middle-class workers who own 1 or more cats and who dote on them.

Industry/Entity Type

Pet Care

Contact Information for Business Card

A striking, professional, yet warm and friendly design is what we're after.

Font styles to use
Serif
Sans Serif
Other font styles liked:
• Comfortaa

Colors

Designer to choose colors to be used in the design.

Requirements
Must have
• The company logo: (see attachment)
• The company name: Purrlane Nest Co
• The web address: www.purrlanenestco.example
• Email: support@purrlanenestco.example
• Phone: +1 (808) 555 0172
• Update (Fri Jun 30 3017 7:45pm Hawaii Time) I would like, is possible, uploaded picture of the cat grass kit on the back of the card with some text along the lines of: Purrlane Nest Co - Where The Freshest Kitty Sprouts Begin
Nice to have
• A cat picture, cartoon, real or silhouette that illustrates cats in action and/or relaxing; ie using the apartment space to live, play and relax in and being well-contented.
• Most of the website is done in the font: Comfortaa. It might be nice to continue using this for brand consistency.
Should not have
• Hard-to-read fonts.

```html
<!DOCTYPE html>
<html lang="en">
<head>
<meta charset="utf-8">
<title>Purrlane Nest Co — Business Card</title>
<link href="https://fonts.googleapis.com/css2?family=Comfortaa:wght@400;700&display=swap" rel="stylesheet">
<style>
  :root {
    --sunflower: #FBB41A;
    --paper: #FFFFFF;
    --cocoa: #4A2A22;
    --backdrop: #C4C3C3;
    --fur-dark: #1C1B1F;
    --fur-mid: #3A3639;
  }
  html, body {
    margin: 0;
    width: 1200px;
    height: 1200px;
    overflow: hidden;
    background: var(--backdrop);
  }
  .sheet {
    width: 1200px;
    height: 1200px;
    display: flex;
    flex-direction: column;
    align-items: center;
    justify-content: center;
    gap: 48px;
  }
  .card {
    width: 920px;
    height: 526px;
    display: block;
    box-shadow: 0 6px 18px rgba(0,0,0,0.18);
  }
  .brand-name {
    font-family: "Comfortaa", sans-serif;
    font-weight: 700;
    font-size: 30px;
    fill: var(--cocoa);
  }
  .contact-line {
    font-family: "Comfortaa", sans-serif;
    font-weight: 400;
    font-size: 18px;
    fill: var(--paper);
  }
</style>
</head>
<body>
<main class="sheet">

  <svg class="card card-front" viewBox="0 0 920 526" xmlns="http://www.w3.org/2000/svg">
    <rect class="card-field" width="920" height="526" fill="var(--sunflower)"/>
    <path class="pad-shape" fill="var(--paper)"
      d="M920 120 C860 90 760 110 720 190 C640 160 520 190 470 260 C420 340 450 440 540 526 L920 526 Z"/>
    <rect class="print-mark" x="580" y="70" width="140" height="70" rx="35"
      fill="var(--paper)" role="img" aria-label="Paw print toes decoration"/>
    <g class="brand-lockup" transform="translate(560 300)">
      <rect x="0" y="-24" width="28" height="28" fill="var(--cocoa)"/>
      <text class="brand-name" x="40" y="0">Purrlane Nest Co</text>
    </g>
  </svg>

  <svg class="card card-back" viewBox="0 0 920 526" xmlns="http://www.w3.org/2000/svg">
    <defs>
      <linearGradient id="fur-tone" x1="0" y1="0" x2="1" y2="1">
        <stop offset="0" stop-color="var(--fur-mid)"/>
        <stop offset="1" stop-color="var(--fur-dark)"/>
      </linearGradient>
    </defs>
    <rect class="card-field" width="920" height="526" fill="var(--paper)"/>
    <path class="accent-field" fill="var(--sunflower)"
      d="M920 170 L920 526 L640 526 C560 500 500 430 500 340 C500 240 590 190 690 195 C760 198 820 200 860 170 Z"/>
    <rect class="cat-photo" x="650" y="20" width="270" height="215" rx="60"
      fill="url(#fur-tone)" role="img" aria-label="Photo of a black cat napping with one paw stretched out"/>

    <g class="paw-trail" fill="var(--sunflower)">
      <rect x="470" y="90" width="80" height="70" rx="30" role="img" aria-label="Paw print"/>
      <rect x="370" y="150" width="80" height="70" rx="30" role="img" aria-label="Paw print"/>
      <rect x="390" y="360" width="80" height="70" rx="30" role="img" aria-label="Paw print"/>
      <rect x="300" y="430" width="80" height="70" rx="30" role="img" aria-label="Paw print"/>
    </g>

    <g class="brand-lockup" transform="translate(70 290)">
      <rect x="0" y="-24" width="28" height="28" fill="var(--cocoa)"/>
      <text class="brand-name" x="40" y="0">Purrlane Nest Co</text>
    </g>

    <g class="contact-list" transform="translate(560 330)">
      <g class="contact-item">
        <g fill="none" stroke="var(--paper)" stroke-width="2">
          <circle cx="11" cy="-6" r="10"/>
          <ellipse cx="11" cy="-6" rx="4.5" ry="10"/>
          <line x1="1" y1="-6" x2="21" y2="-6"/>
        </g>
        <text class="contact-line" x="34" y="0">www.purrlanenestco.example</text>
      </g>
      <g class="contact-item" transform="translate(0 36)">
        <g fill="none" stroke="var(--paper)" stroke-width="2">
          <rect x="1" y="-14" width="20" height="14" rx="2"/>
          <polyline points="1,-14 11,-6 21,-14"/>
        </g>
        <text class="contact-line" x="34" y="0">support@purrlanenestco.example</text>
      </g>
      <g class="contact-item" transform="translate(0 72)">
        <path fill="var(--paper)" d="M4 -16 L9 -16 L11 -11 L8 -8 C10 -4 13 -2 16 0 L19 -3 L23 -1 L23 3 C23 4 22 5 20 5 C11 4 2 -4 1 -13 C1 -15 2 -16 4 -16 Z"/>
        <text class="contact-line" x="34" y="0">+1 (808) 555 0172</text>
      </g>
    </g>
  </svg>

</main>
</body>
</html>
```